Exec Conference Design Concept

We need to refresh & update nonprofit association graphic design for annual meeting. The graphics will be used to promote the event primarily through digital communications & social media. Other materials we generate for this event are the agenda & billboard content. You can view the existing design at www.lumivarguild.org under Events.

The target audience is primarily male, ages 35-60 in executive positions in C-Corps. The conference topics center on manufacturing regulations, marketing trends, and the economy. This conference has been around almost 30 years so we need something to invigorate potential registrants that will get their attention. It still needs to be professional and business-like.

In addition to a new design concept we would like to update the color palette. We’ve attached some mood boards with potential color & font suggestions. Our company logo is also attached and is the only design element tied to our branding that cannot be changed.

Designs should be energetic and sophisticated. Ideally, we would like the designs in Adobe Indesign or Photoshop. However, we can work with Illustrator.

Target Market(s)

Male business executives age 35-60.

Industry/Entity Type

Polystyrene manufacturing industry supply chain.

Font styles to use
Other font styles liked:
• I usually prefer sans serif

Requirements
Must have
• Focus points to draw attention to higher level informational units. For example, some people will only read the headers and not detailed copy.
Nice to have
• Ways to insert bonus content that don’t over power other content. I like to see a good use of white space to enhance readability.

```html
<!DOCTYPE html>
<html lang="en">
<head>
<meta charset="utf-8">
<title>LVG Forum – Email Concepts</title>
<link rel="stylesheet" href="https://fonts.googleapis.com/css2?family=Barlow:wght@500;600;700;800&family=Barlow+Semi+Condensed:wght@500;600&family=Source+Sans+3:wght@400;600&display=swap">
<style>
:root{
  --navy:#1b3766;
  --navy-deep:#142a52;
  --orange:#e4621c;
  --orange-dark:#c84f12;
  --ink:#2b2f36;
  --muted:#5b6068;
  --rule:#d9dce1;
  --panel:#eef0f3;
  --white:#ffffff;
  --page:#ffffff;
}
*{box-sizing:border-box;margin:0;padding:0}
html,body{width:1200px;height:810px;overflow:hidden;background:var(--page)}
body{position:relative;font-family:"Barlow",Arial,sans-serif;color:var(--ink)}

.brand{display:flex;align-items:center;justify-content:center;gap:.3em;color:var(--navy);font-weight:800;letter-spacing:.01em;line-height:1;white-space:nowrap}
.brand-mark{width:.55em;height:.55em;background:var(--orange);display:inline-block;flex:none}

.board-logo{position:absolute;left:205px;top:66px;width:440px;font-size:58px}
.caption{position:absolute;font-family:"Source Sans 3",Arial,sans-serif;font-size:18px;color:var(--muted);text-align:center;white-space:nowrap}
.caption-logo{left:265px;top:146px;width:380px;font-size:17px}
.board-rule{position:absolute;left:89px;top:195px;width:1012px;height:1px;background:var(--rule)}

.email{position:absolute;background:var(--white);box-shadow:0 1px 6px rgba(0,0,0,.18);overflow:hidden;display:flex;flex-direction:column}
.email-desktop{left:89px;top:246px;width:385px;height:484px}
.email-mobile{left:530px;top:366px;width:249px;height:351px}
.email-phone{left:852px;top:344px;width:205px;height:353px}

.email-head{display:flex;flex-direction:column;justify-content:center;text-align:center;background:var(--white);flex:none}
.tagline{font-size:11px;font-weight:700;color:var(--navy);margin-top:8px;white-space:nowrap}
.hero{position:relative;display:flex;align-items:center;justify-content:center;color:var(--white);font-family:"Barlow Semi Condensed",Arial,sans-serif;font-weight:600;text-align:center;flex:none;white-space:nowrap;
  background:linear-gradient(180deg,#2a3d63 0%,#1d2f52 45%,#6b4a2a 80%,#c98434 100%)}
.hero-accent{position:absolute;left:0;right:0;top:0;height:6px;background:linear-gradient(90deg,var(--navy) 0%,#8a93a3 50%,var(--orange) 100%)}
.hero span{position:relative;text-shadow:0 1px 3px rgba(0,0,0,.5)}

.content{background:var(--panel);text-align:center;flex:none}
.section-title{color:var(--navy);font-weight:600;white-space:nowrap}
.topics{list-style:none;text-align:left;color:var(--ink)}
.topics li{position:relative;white-space:nowrap}
.topics li::before{content:"";position:absolute;left:0;top:.5em;width:4px;height:4px;border-radius:50%;background:var(--orange)}
.divider{height:1px;background:var(--rule)}
.speakers{display:flex;justify-content:center}
.speaker{text-align:center}
.speaker-photo{display:block;background:linear-gradient(180deg,#c9ccd1 0%,#9aa1ab 55%,#2f3a4f 100%)}
.speaker-name{display:block;color:var(--navy);font-weight:600;white-space:nowrap}

.cta{display:inline-block;background:linear-gradient(180deg,var(--orange) 0%,var(--orange-dark) 100%);color:var(--white);font-weight:700;text-transform:uppercase;border-radius:3px;white-space:nowrap}

.sponsors{background:var(--white);text-align:center;display:flex;flex-direction:column;justify-content:center;flex:none}
.sponsor-label{display:flex;align-items:center;justify-content:center;gap:8px;font-weight:700;color:var(--ink)}
.sponsor-label::before,.sponsor-label::after{content:"";height:1px;background:var(--rule);flex:0 0 60px}
.sponsor-row{display:flex;justify-content:center;align-items:center}
.sponsor{display:flex;align-items:center;gap:4px;font-weight:700;color:var(--navy);white-space:nowrap}
.sponsor i{display:inline-block;border-radius:50%;background:var(--orange)}

.footer{background:var(--navy);color:var(--white);text-align:center;font-family:"Source Sans 3",Arial,sans-serif;font-weight:600;margin-top:auto;display:flex;align-items:center;justify-content:center;white-space:nowrap;flex:none}

/* desktop sizing */
.email-desktop .email-head{height:80px}
.email-desktop .email-head .brand{font-size:32px}
.email-desktop .hero{height:92px;font-size:19px}
.email-desktop .content{height:226px;padding:12px 24px 0}
.email-desktop .section-title{font-size:14px}
.email-desktop .topics{margin:8px 0 8px 30px;font-size:11px;line-height:17px}
.email-desktop .topics li{padding-left:10px}
.email-desktop .speakers-title{margin-top:8px;font-size:13px}
.email-desktop .speakers{gap:14px;margin-top:7px}
.email-desktop .speaker-photo{width:82px;height:76px}
.email-desktop .sponsors{height:58px}
.email-desktop .sponsor-label{font-size:8px}
.email-desktop .sponsor-row{gap:28px;margin-top:8px}
.email-desktop .sponsor{font-size:12px}
.email-desktop .sponsor i{width:9px;height:9px}
.email-desktop .footer{font-size:9px;height:28px}

/* mobile sizing */
.email-mobile .email-head{height:56px}
.email-mobile .email-head .brand{font-size:24px}
.email-mobile .hero{height:74px;font-size:12px;align-items:flex-start;padding-top:16px}
.email-mobile .hero-accent{height:3px}
.email-mobile .content{height:93px;display:flex;align-items:center;justify-content:center}
.email-mobile .speakers{gap:8px}
.email-mobile .speaker-photo{width:58px;height:56px}
.email-mobile .speaker-name{font-size:8px;margin-top:3px}
.email-mobile .cta-row{background:var(--white);display:flex;align-items:center;justify-content:center;height:50px;flex:none}
.email-mobile .cta{font-size:10px;padding:7px 32px}
.email-mobile .sponsors{height:56px;background:var(--panel)}
.email-mobile .sponsor-label{font-size:7px}
.email-mobile .sponsor-label::before,.email-mobile .sponsor-label::after{flex-basis:30px}
.email-mobile .sponsor-row{gap:14px;margin-top:7px}
.email-mobile .sponsor{font-size:8px}
.email-mobile .sponsor i{width:6px;height:6px}
.email-mobile .footer{font-size:6px;height:22px}

/* phone-width sizing */
.email-phone .email-head{height:43px}
.email-phone .email-head .brand{font-size:20px}
.email-phone .hero{height:60px;font-size:10px;align-items:flex-start;padding-top:10px}
.email-phone .hero-accent{height:3px}
.email-phone .content{padding:12px 12px 6px;flex:1 1 auto}
.email-phone .section-title{font-size:10px}
.email-phone .topics{margin:7px 0 7px 8px;font-size:8px;line-height:14px}
.email-phone .topics li{padding-left:8px}
.email-phone .speakers{gap:6px;margin-top:8px}
.email-phone .speaker-photo{width:44px;height:44px}
.email-phone .speaker-name{font-size:7px;margin-top:2px}
.email-phone .cta{font-size:9px;padding:7px 30px;margin-top:12px}
.email-phone .footer{font-size:10px;height:27px}

.caption-desktop{left:89px;top:748px;width:385px}
.caption-mobile{left:530px;top:748px;width:249px}
.caption-phone{left:840px;top:756px;width:236px}
</style>
</head>
<body>

<div class="brand board-logo"><span class="brand-mark"></span>LVG FORUM</div>
<div class="caption caption-logo">Updated Logo</div>
<div class="board-rule"></div>

<article class="email email-desktop">
  <header class="email-head">
    <div class="brand"><span class="brand-mark"></span>LVG FORUM</div>
    <p class="tagline">Regulation • Communication • Economics Conference 2022</p>
  </header>
  <div class="hero" role="img" aria-label="Industrial plant skyline lit at dusk">
    <div class="hero-accent"></div>
    <span>Advancing Manufacturing Together</span>
  </div>
  <section class="content">
    <h2 class="section-title">Join Us for Industry Insights &amp; Networking</h2>
    <ul class="topics">
      <li>Regulatory Updates</li>
      <li>Economic Trends</li>
      <li>Effective Communication Strategies</li>
    </ul>
    <div class="divider"></div>
    <h3 class="section-title speakers-title">Featured Speakers</h3>
    <div class="speakers">
      <span class="speaker-photo" role="img" aria-label="Portrait of speaker Owen Hale"></span>
      <span class="speaker-photo" role="img" aria-label="Portrait of speaker Nora Pike"></span>
      <span class="speaker-photo" role="img" aria-label="Portrait of speaker Reid Calder"></span>
    </div>
  </section>
  <section class="sponsors">
    <p class="sponsor-label">Sponsored by:</p>
    <div class="sponsor-row">
      <span class="sponsor"><i></i>Corvane</span>
      <span class="sponsor"><i></i>Tessaly</span>
      <span class="sponsor"><i></i>Brightmol</span>
    </div>
  </section>
  <footer class="footer">www.lvgforum.org &nbsp;|&nbsp; info@lvgforum.org &nbsp;|&nbsp; (555) 014-2290</footer>
</article>
<div class="caption caption-desktop">Email Design – Desktop</div>

<article class="email email-mobile">
  <header class="email-head">
    <div class="brand"><span class="brand-mark"></span>LVG FORUM</div>
  </header>
  <div class="hero" role="img" aria-label="Industrial plant skyline lit at dusk">
    <div class="hero-accent"></div>
    <span>Advancing Manufacturing Together</span>
  </div>
  <section class="content">
    <div class="speakers">
      <div class="speaker"><span class="speaker-photo" role="img" aria-label="Portrait of speaker Owen Hale"></span><span class="speaker-name">Owen Hale</span></div>
      <div class="speaker"><span class="speaker-photo" role="img" aria-label="Portrait of speaker Nora Pike"></span><span class="speaker-name">Nora Pike</span></div>
      <div class="speaker"><span class="speaker-photo" role="img" aria-label="Portrait of speaker Reid Calder"></span><span class="speaker-name">Reid Calder</span></div>
    </div>
  </section>
  <div class="cta-row"><span class="cta">Register Now</span></div>
  <section class="sponsors">
    <p class="sponsor-label">Sponsored by:</p>
    <div class="sponsor-row">
      <span class="sponsor"><i></i>Corvane</span>
      <span class="sponsor"><i></i>Tessaly</span>
      <span class="sponsor"><i></i>Brightmol</span>
    </div>
  </section>
  <footer class="footer">www.lvgforum.org | info@lvgforum.org | (555) 014-2290</footer>
</article>
<div class="caption caption-mobile">Email Design – Mobile</div>

<article class="email email-phone">
  <header class="email-head">
    <div class="brand"><span class="brand-mark"></span>LVG FORUM</div>
  </header>
  <div class="hero" role="img" aria-label="Industrial plant skyline lit at dusk">
    <div class="hero-accent"></div>
    <span>Advancing Manufacturing Together</span>
  </div>
  <section class="content">
    <h2 class="section-title">Industry Insights &amp; Networking</h2>
    <ul class="topics">
      <li>Regulatory Updates</li>
      <li>Economic Trends</li>
      <li>Effective Communication Strategies</li>
    </ul>
    <div class="divider"></div>
    <div class="speakers">
      <div class="speaker"><span class="speaker-photo" role="img" aria-label="Portrait of speaker Owen Hale"></span><span class="speaker-name">Owen Hale</span></div>
      <div class="speaker"><span class="speaker-photo" role="img" aria-label="Portrait of speaker Nora Pike"></span><span class="speaker-name">Nora Pike</span></div>
      <div class="speaker"><span class="speaker-photo" role="img" aria-label="Portrait of speaker Reid Calder"></span><span class="speaker-name">Reid Calder</span></div>
    </div>
    <span class="cta">Register Now</span>
  </section>
  <footer class="footer">www.lvgforum.org</footer>
</article>
<div class="caption caption-phone">Email Design – Mobile</div>

</body>
</html>
```